Lakeshore Freightways Guild Web Update

Update wordpress based association web site. Please look up www.lakeshorefreightwaysguild.com for our web site to get a feel for what we currently having. We would like our updated web site to look similar to: www.brightoakline.com. We will provide our key points for updating in a future email.

Target Market(s)

duplicate the brightoakline.com format please.

Number of Pages Required

4 page

Font styles to use
Serif

Requirements
Must have
• duplicate the brightoakline.com format please. You will keep most of the content that we currently have on our website.
Nice to have
• n/a
Should not have
• n/a

```html
<!DOCTYPE html>
<html lang="en">
<head>
<meta charset="utf-8">
<title>Lakeshore Freightways Guild</title>
<link rel="stylesheet" href="https://fonts.googleapis.com/css2?family=Raleway:wght@400;500;700&family=Playfair+Display:wght@400;700&display=swap">
<style>
:root{
  --navy:#15318e;
  --navy-dark:#0f2366;
  --periwinkle:#4a62a6;
  --card:#c5cbe3;
  --accent:#e5492f;
  --white:#ffffff;
  --ink:#3a3f52;
}
*{box-sizing:border-box;margin:0;padding:0}
html,body{width:1198px;height:1200px;overflow:hidden}
body{font-family:'Raleway',sans-serif;background:var(--periwinkle);position:relative}
.site-header{position:absolute;left:0;top:0;width:1198px;height:120px;background:linear-gradient(90deg,var(--navy),var(--navy-dark))}
.brand{position:absolute;left:120px;top:26px;width:110px;color:var(--white);font-family:'Playfair Display',serif;font-size:16px;line-height:18px;font-weight:400;border-bottom:2px solid var(--white);padding-bottom:3px}
.main-nav{position:absolute;left:329px;top:52px;display:flex;gap:24px}
.main-nav a{color:var(--white);text-decoration:none;font-size:14.5px;font-weight:500;letter-spacing:-.2px}
.search{position:absolute;left:880px;top:44px;width:200px;height:32px;border:2px solid var(--white);border-radius:3px;display:flex}
.search span{flex:1;color:var(--white);font-size:12px;padding:7px 0 0 14px}
.search b{width:32px;background:var(--accent);display:flex;align-items:center;justify-content:center}
.hero{position:absolute;left:0;top:120px;width:1198px;height:480px;background:linear-gradient(160deg,#e8eaef 0%,#c9ccd4 45%,#dfe1e6 70%,#b9bcc4 100%)}
.hero-caption{position:absolute;left:521px;top:80px;width:480px;height:320px;background:rgba(110,110,115,.72);color:var(--white);font-size:12px;font-weight:500;line-height:19px;padding:76px 50px 0 53px;text-transform:uppercase}
.dots{position:absolute;left:556px;top:448px;display:flex;gap:8px}
.dots i{width:16px;height:16px;border:2px solid var(--accent);border-radius:50%;display:flex;align-items:center;justify-content:center}
.dots i.on::after{content:"";width:6px;height:6px;border-radius:50%;background:var(--accent)}
.welcome{position:absolute;left:0;top:600px;width:1198px;height:240px;background:var(--navy);color:var(--white)}
.avatar{position:absolute;left:161px;top:53px;width:134px;height:134px;border-radius:50%;border:3px solid var(--white);background:radial-gradient(circle at 50% 40%,#8a7a6e,#4a4a52 60%,#2a2a30)}
.welcome p{position:absolute;left:336px;top:59px;width:750px;font-size:12px;line-height:19.2px}
.signature{position:absolute;left:337px;top:133px;font-size:11.5px}
.signature strong{display:block;font-size:13px;font-weight:700}
.card{position:absolute;top:905px;width:472px;height:280px;background:var(--card);border-radius:3px;text-align:center}
.card .icon{width:64px;height:64px;border-radius:50%;background:var(--accent);margin:32px auto 0;display:flex;align-items:center;justify-content:center}
.card h2{font-family:'Playfair Display',serif;color:var(--accent);font-size:21px;font-weight:700;margin-top:13px;letter-spacing:-.3px}
.card p{font-size:12px;line-height:19.2px;color:var(--ink);margin:8px 26px 0}
</style>
</head>
<body>
<header class="site-header">
  <div class="brand">Lakeshore Freightways Guild</div>
  <nav class="main-nav">
    <a href="#">HOME</a><a href="#">WHAT WE DO</a><a href="#">WHO WE ARE</a><a href="#">WHO WE SERVE</a><a href="#">RESOURCES</a>
  </nav>
  <div class="search"><span>Search here</span><b><svg width="18" height="18" viewBox="0 0 18 18"><circle cx="7" cy="7" r="5" fill="none" stroke="#fff" stroke-width="2"/><line x1="10.5" y1="10.5" x2="16" y2="16" stroke="#fff" stroke-width="2.5"/></svg></b></div>
</header>

<section class="hero" role="img" aria-label="Red electric freight train crossing a snowy mountain valley">
  <div class="hero-caption">Every year America's freight railroads spend more than $20 billion annually of their own funds, not taxpayer money, to build and maintian a rail network that is safe, reliable, efficient and affordable.</div>
  <div class="dots"><i class="on"></i><i></i><i></i><i></i></div>
</section>

<section class="welcome">
  <div class="avatar" role="img" aria-label="Portrait of the association president"></div>
  <p>I would like to welcome you to the Lakeshore Freightways Guild website. Here you will find valuable information on the Lakeshore region railroads, including issues and concerns in and around the railroad industry. We are an active state railroad association and we look forward to contuinued success with our partnerships. Please make sure to click on our member railroad company links while you're here. Also, sign up for our newsletter and follow the LFG n Chirpline. Thank you and I hope you enjoy your visit to our website.</p>
  <div class="signature"><strong>Dale Hartman</strong>President</div>
</section>

<article class="card" style="left:120px">
  <div class="icon"><svg width="40" height="40" viewBox="0 0 40 40" fill="none" stroke="#fff" stroke-width="2"><line x1="20" y1="4" x2="20" y2="36"/><path d="M8 9h22l4 4-4 4H8z"/><path d="M32 19H10l-4 4 4 4h22z"/></svg></div>
  <h2>WHAT WE DO</h2>
  <p>The LFG reviews all introduced legislation in the House and Senate. Proposed legislation affecting the rail industry is shared with our members. Final industry positions regarding legislation are then communicated to the legislature. We pursue the same activity with appropriate personnel in the state departments and the legislative rules process.</p>
</article>

<article class="card" style="left:608px">
  <div class="icon"><svg width="44" height="44" viewBox="0 0 44 44"><circle cx="22" cy="22" r="19" fill="#fff"/><g fill="none" stroke="#e5492f" stroke-width="2"><circle cx="17" cy="17" r="5"/><circle cx="27" cy="17" r="5"/><path d="M8 32c0-6 4-9 9-9s9 3 9 9z"/><path d="M18 32c0-6 4-9 9-9s9 3 9 9z"/></g></svg></div>
  <h2>WHO WE ARE</h2>
  <p>The Lakeshore Freightways Guild (LFG) is a non-profit trade association that represents the interests of freight railroads operating in the Lakeshore region. LFG members range in size from large Class 1 interstate carriers to smaller regional carriers and shortline railroads. LFG members account for over 95% of all freight rail moved in the Lakeshore region.</p>
</article>
</body>
</html>
```